Business card and logo designs

We are looking to create a cool and trendy image for the company, some thing what quince has. We already have a logo, but we can reconsider a new logo.

Vorilo provides a new kind of web service for businesses to take appointments using web and mobile. Usually a customer needs to call or check several times. Vorilo solves this trouble. Our service refills cancellations quickly and automatically plus reduces no-shows. On top of that, our analytical tools give deep business and customer insights to increase revenue.

Phone bookings and cancellations are frustrating, time-consuming and expensive.It can take hours to book a 20 min appointment for e.g. with your doctor. When customers don’t find a suitable time, they need to call or check online again and again. Vorilo turn the tables and enables your doctor to get back to you with appointment of your choice,automatically. It refills cancellations quickly and automatically. Vrolio did not invent a booking system, like Quince did not invest a mobile phone. However, we make it mobile, intelligent and useful.

Vorilo identity should present a change, the same one which quince brought to mobile. Despite the fact that booking systems has been around for 2 decades, we change the game.

We want to communicate that we are saving time for consumers and businesses in an an innovative way and helping businesses to improve revenue.

Reason: We want more design entries.

Contents of the business card....

But we want the empty template so when new people join, we use the same.

Bram Tolvek

+358-402739158

Founder & CEO 

bram.tolvek@vorilo-example.net

 Vorilo Solutions Oy

Helsinki, Finland

www.vorilo-example.net

All,

We have to get ideas about a new logo. New business card is not enough.

Reason: More designs needed...

Reason: We have got very few good designs so far.

Reason: Need a bite more time... our creative director was busy

Target Market(s)

Most developed countries

Industry/Entity Type

Doctor

Requirements
Must have
• Color orange and green....
Should not have
• Should not have the obvious things... more intelligent design...

```html
<!DOCTYPE html>
<html lang="en">
<head>
<meta charset="utf-8">
<title>Vorilo Business Card</title>
<link rel="stylesheet" href="https://fonts.googleapis.com/css2?family=Poppins:wght@500;600&family=Questrial&display=swap">
<style>
  :root {
    --teal: #13766b;
    --orange: #f7941d;
    --ink: #111111;
    --page: #fefefe;
    --card-start: #ffffff;
    --card-end: #f2f4f6;
  }
  html, body {
    margin: 0;
    width: 1200px;
    height: 900px;
    overflow: hidden;
    background: var(--page);
  }
  .canvas {
    position: relative;
    width: 1200px;
    height: 900px;
  }
  .card {
    position: absolute;
    left: 255px;
    top: 194px;
    width: 770px;
    height: 471px;
    background: linear-gradient(90deg, var(--card-start) 0%, var(--card-end) 100%);
    box-shadow: 0 6px 28px rgba(0, 0, 0, 0.10);
    overflow: hidden;
  }
  .brand {
    position: absolute;
    left: 30px;
    top: 176px;
    display: flex;
    align-items: center;
    gap: 12px;
  }
  .brand-mark {
    width: 14px;
    height: 14px;
    background: var(--orange);
  }
  .brand-name {
    font-family: "Poppins", sans-serif;
    font-weight: 500;
    font-size: 56px;
    line-height: 1;
    color: var(--ink);
    letter-spacing: 0.5px;
  }
  .contact {
    position: absolute;
    left: 450px;
    top: 160px;
  }
  .contact-name {
    position: relative;
    margin: 0;
    font-family: "Poppins", sans-serif;
    font-weight: 600;
    font-size: 27px;
    line-height: 34px;
    color: var(--teal);
    padding-left: 18px;
  }
  .contact-name::before {
    content: "";
    position: absolute;
    left: 0;
    top: 11px;
    width: 12px;
    height: 12px;
    background: var(--orange);
  }
  .contact-email {
    margin: 0;
    padding-left: 18px;
    font-family: "Questrial", sans-serif;
    font-size: 19px;
    line-height: 28px;
    color: var(--teal);
  }
  .contact-role {
    margin: 8px 0 0;
    padding-left: 18px;
    font-family: "Poppins", sans-serif;
    font-weight: 600;
    font-size: 19px;
    line-height: 26px;
    color: var(--teal);
  }
  .bands {
    position: absolute;
    left: 0;
    top: 391px;
    width: 770px;
    height: 24px;
  }
  .footer {
    position: absolute;
    left: 0;
    right: 0;
    top: 428px;
    margin: 0;
    text-align: center;
    font-family: "Poppins", sans-serif;
    font-weight: 600;
    font-size: 16px;
    line-height: 24px;
    color: var(--teal);
  }
</style>
</head>
<body>
<div class="canvas">
  <section class="card">
    <div class="brand">
      <span class="brand-name">Vorilo</span>
      <span class="brand-mark"></span>
    </div>

    <div class="contact">
      <h1 class="contact-name">Bram Tolvek</h1>
      <p class="contact-email">bram.tolvek@vorilo-example.net</p>
      <p class="contact-role">Founder &amp; CEO</p>
    </div>

    <svg class="bands" viewBox="0 0 770 24" aria-hidden="true">
      <rect x="0" y="0" width="770" height="12" fill="var(--teal)"/>
      <rect x="0" y="12" width="770" height="12" fill="var(--orange)"/>
    </svg>

    <p class="footer">Vorilo Solutions Oy, Helsinki, Finland 358-402739158 | www.vorilo-example.net</p>
  </section>
</div>
</body>
</html>
```